Redesigning Web Pages

I need to redesign a section on my website:
http://kefor.mb-gemwork.com/en/copperleafden
The complete (Copperleaf Den) section needs to be redesigned.
The works involves designing only. I have my own development team. You would need to provide me with the designing (psd) files at the end of the project.
Please go through the whole section so that you can see the pages that needs to be redesigned (Note: you can create a demo account to see the inner pages, its ok as this link is on the development server). Again, to be clear, I need only to redesign this section (including its sub pages, like registration, user profile page, etc), not the whole website. Of course, the main page to be designed would be the section "main page" the other inner pages are to match the design of the main section page.
All features, functions, and facilities provided on the section are to remain the same.
The design needs to match the current website format. Keep in mind the look and feel information I have provided for this section. Note: Please view the highlighted area in the attached file. This is the area that needs to be redesigned.
The design would be selected based on the creativity of the designer and understanding of what needs to be done.

```html
<!DOCTYPE html>
<html lang="en">
<head>
<meta charset="utf-8">
<title>Kefor – Copperleaf Den</title>
<link href="https://fonts.googleapis.com/css2?family=Arimo:wght@400;700&display=swap" rel="stylesheet">
<style>
:root{
  --green:#7ea82b;
  --green-dark:#5f8419;
  --ink:#333;
  --muted:#666;
  --bar:#3b3b3b;
  --bg:#ececec;
  --panel:#fff;
  --line:#d6d6d6;
  --gold:#f0a81a;
  --footer:#2a2a2a;
  --footer-text:#bdbdbd;
}
*{box-sizing:border-box;margin:0;padding:0}
html,body{width:763px;height:1200px;overflow:hidden}
body{background:var(--bg);font-family:"Arimo",Arial,sans-serif;color:var(--ink);font-size:9px;position:relative}
.abs{position:absolute}

/* header */
.header{left:0;top:0;width:763px;height:160px;background:#f4f1ea}
.header-photo{left:170px;top:0;width:593px;height:160px;background:linear-gradient(100deg,#e8dcc4 0%,#c9a77a 35%,#8c6a48 60%,#d9c6a4 85%,#f1e7d3 100%)}
.logo{left:18px;top:22px;display:flex;align-items:center;gap:8px;font-size:26px;font-weight:700;color:var(--green)}
.logo .dot{width:22px;height:22px;border-radius:50%;background:var(--green)}
.lang{right:24px;top:24px;display:flex;gap:6px;align-items:center;color:#fff;font-size:10px}
.lang .btn{background:var(--gold);color:#fff;padding:3px 10px;font-weight:700;font-size:9px}
.search{right:24px;top:64px;display:flex;gap:6px;align-items:center}
.search .field{width:130px;height:20px;background:#fff;border:1px solid #bbb;color:#999;padding:4px 6px;font-size:9px}
.search .go{background:var(--green);width:22px;height:20px}

/* nav */
.nav{left:0;top:167px;width:763px;height:28px;background:var(--green);display:flex;align-items:center;padding-left:14px;color:#fff;font-size:10px}
.nav span{padding:0 7px;border-left:1px solid rgba(255,255,255,.5)}
.nav span:first-child{border-left:0}
.nav .active{background:var(--green-dark);padding:8px 9px}

/* login */
.login{left:0;top:201px;width:763px;height:30px;background:#fff;border-bottom:1px solid var(--line);display:flex;align-items:center;padding-left:20px;gap:8px;font-size:9px}
.login .field{width:78px;height:16px;border:1px solid #ccc;color:#999;padding:2px 4px}
.login .btn{background:var(--gold);color:#fff;font-weight:700;padding:3px 8px}

/* panels */
.panel{background:var(--panel);border:1px solid var(--line)}
.tab-head{height:24px;background:var(--bar);color:#fff;font-weight:700;font-size:10px;display:flex;align-items:center;padding-left:12px}
.tab-head.green{background:var(--green)}
.foot-bar{position:absolute;left:0;right:0;bottom:0;height:22px;display:flex;justify-content:space-between;align-items:center;background:#f3f3f3;border-top:1px solid var(--line)}
.foot-bar .dark{background:var(--bar);color:#fff;font-weight:700;font-size:8.5px;padding:6px 12px;height:22px}
.foot-bar .green{background:var(--green);color:#fff;font-weight:700;font-size:8.5px;padding:6px 14px;height:22px}

.stories{left:20px;top:253px;width:520px;height:335px}
.photo-card{position:absolute;width:150px;height:122px}
.photo-card .back{position:absolute;inset:0;background:#fff;border:1px solid #ccc;transform:rotate(-4deg);box-shadow:0 1px 3px rgba(0,0,0,.15)}
.photo-card .front{position:absolute;inset:0;background:#fff;border:1px solid #ccc;padding:6px;box-shadow:0 1px 3px rgba(0,0,0,.2)}
.photo-card .pic{height:90px}
.photo-card .cap{display:flex;justify-content:space-between;margin-top:6px;font-size:7px}
.photo-card .cap b{color:var(--gold)}
.pic.valley{background:linear-gradient(180deg,#9fb9c9 0%,#6d8f4a 55%,#3f6a2a 100%)}
.pic.bloom{background:radial-gradient(circle at 45% 50%,#f6c23a 0%,#f08a1c 45%,#6a8a2c 100%)}

.articles{left:563px;top:253px;width:180px;height:335px}
.articles .tab-head{justify-content:center}
.articles .tab-head em{font-style:normal;color:var(--gold);margin-left:3px}
.article{padding:6px 12px 2px}
.article b{color:var(--green);font-size:9px}
.article p{font-size:7.5px;line-height:1.35;color:var(--muted)}

/* reviews */
.reviews-title{left:20px;top:600px;font-size:17px;font-weight:700;color:var(--ink)}
.reviews-title span{color:var(--green)}
.reviews{left:20px;top:628px;width:723px;height:145px}
.tabs{display:flex;gap:4px;padding:6px 10px 0;border-bottom:2px solid var(--green)}
.tabs span{padding:6px 20px;font-weight:700;font-size:8.5px;background:var(--green);color:#fff}
.tabs .on{background:#fff;color:var(--ink);border:1px solid var(--line);border-bottom:0}
.reviews .body{padding:8px 12px;font-size:8px;line-height:1.5;color:var(--muted)}

/* stats boxes */
.stat{top:805px;width:173px;height:185px}
.stat .head{height:24px;background:var(--green);color:#fff;font-weight:700;font-size:8.5px;display:flex;align-items:center;padding-left:10px}
.stat .head.light{background:#fff;color:var(--ink);border-bottom:2px solid var(--green)}
.stat ul{list-style:none;padding:8px 12px}
.stat li{display:flex;align-items:center;gap:6px;font-size:8.5px;padding:3px 0}
.stat li svg{flex:none}
.stat li small{color:var(--green);font-size:7.5px}
.stat .more{position:absolute;left:0;right:0;bottom:0;height:22px;background:var(--bar);color:#fff;font-size:8.5px;display:flex;align-items:center;padding:0 10px}
.stat .more.right{justify-content:flex-end;font-weight:700}

/* footer */
.foot-nav{left:0;top:1008px;width:763px;height:22px;background:var(--green);display:flex;align-items:center;justify-content:center;color:#fff;font-size:8.5px}
.foot-nav span{padding:0 8px;border-left:1px solid rgba(255,255,255,.5)}
.foot-nav span:first-child{border-left:0}
.footer{left:0;top:1030px;width:763px;height:170px;background:var(--footer);color:var(--footer-text)}
.fcol{position:absolute;top:16px;width:200px}
.fcol h4{color:#fff;font-size:10px;margin-bottom:8px}
.fcol p{font-size:8px;line-height:1.7}
.copy{position:absolute;right:24px;bottom:10px;font-size:7.5px}
</style>
</head>
<body>

<div class="abs header"></div>
<div class="abs header-photo" role="img" aria-label="Hotel interior and travel scenes banner"></div>
<div class="abs logo"><span class="dot"></span>KEFOR</div>
<div class="abs lang">Languages <span class="btn">English</span><span class="btn">Other</span></div>
<div class="abs search"><span class="field">Search</span><span class="go"></span></div>

<nav class="abs nav">
  <span>Destinations</span><span>Things to do</span><span>Hotels</span><span>Weather</span><span>Maps</span><span>Tours</span><span>Travel Photos</span><span>Travel Articles</span><span>Currency Converter</span><span class="active">Copperleaf Den</span>
</nav>

<div class="abs login">
  <b>Login:</b><span class="field">Username</span><span class="field">Password</span><span class="btn">LOGIN</span>
  <span>Forgot Password</span><span>|</span><span>Register</span>
</div>

<section class="abs panel stories">
  <div class="tab-head">Share Your Travel Stories and Photos</div>
  <div class="photo-card" style="left:40px;top:46px"><div class="back"></div><div class="front"><div class="pic valley" role="img" aria-label="Green valley landscape photo"></div><div class="cap"><b>Title</b><span>Source : Author</span></div></div></div>
  <div class="photo-card" style="left:230px;top:46px"><div class="back"></div><div class="front"><div class="pic valley" role="img" aria-label="Lake and hills landscape photo"></div><div class="cap"><b>Title</b><span>Source : Author</span></div></div></div>
  <div class="photo-card" style="left:40px;top:182px"><div class="back"></div><div class="front"><div class="pic bloom" role="img" aria-label="Orange flowers photo"></div><div class="cap"><b>Title</b><span>Source : Author</span></div></div></div>
  <div class="photo-card" style="left:230px;top:182px"><div class="back"></div><div class="front"><div class="pic bloom" role="img" aria-label="Orange flowers photo"></div><div class="cap"><b>Title</b><span>Source : Author</span></div></div></div>
  <div class="foot-bar"><span class="dark">Submit Your Travel Photos</span><span class="green">View All</span></div>
</section>

<aside class="abs panel articles">
  <div class="tab-head green">Latest<em>ARTICLES</em></div>
  <div class="article"><b>Lorem</b><p>Lorem ipsum dolor sit amet, consectetur adipiscing elit, sed do eiusmod tempor.</p></div>
  <div class="article"><b>Lorem</b><p>Lorem ipsum dolor sit amet, consectetur adipiscing elit, sed do eiusmod tempor.</p></div>
  <div class="article"><b>Lorem</b><p>Lorem ipsum dolor sit amet, consectetur adipiscing elit, sed do eiusmod tempor.</p></div>
  <div class="article"><b>Lorem</b><p>Lorem ipsum dolor sit amet, consectetur adipiscing elit, sed do eiusmod tempor.</p></div>
  <div class="article"><b>Lorem</b><p>Lorem ipsum dolor sit amet, consectetur adipiscing elit.</p></div>
  <div class="foot-bar"><span class="dark">Submit Your Story</span><span class="green">More News</span></div>
</aside>

<h2 class="abs reviews-title">Latest <span>Reviews</span></h2>
<section class="abs panel reviews">
  <div class="tabs"><span class="on">THINGS TO DO</span><span>TOURS</span><span>HOTELS</span></div>
  <div class="body">
    <p>Lorem ipsum dolor sit amet, consectetur adipiscing elit, sed do eiusmod tempor incididunt ut labore et dolore magna aliqua. Ut enim ad minim veniam, quis nostrud exercitation ullamco laboris nisi ut aliquip ex ea commodo consequat duis aute irure dolor in reprehenderit in voluptate.</p>
    <p>Velit esse cillum dolore eu fugiat nulla pariatur. Excepteur sint occaecat cupidatat non proident, sunt in culpa qui officia deserunt mollit anim id est laborum sed ut perspiciatis unde omnis iste natus error sit voluptatem accusantium doloremque laudantium totam rem aperiam.</p>
  </div>
  <div class="foot-bar"><span class="dark">Submit Your Reviews</span><span class="green">View All</span></div>
</section>

<section class="abs panel stat" style="left:20px">
  <div class="head">Recent Registered Users</div>
  <ul>
    <li><svg width="8" height="8"><path d="M1 1l6 3-6 3z" fill="#7ea82b"/></svg>Dalvennor</li>
    <li><svg width="8" height="8"><path d="M1 1l6 3-6 3z" fill="#7ea82b"/></svg>Lowen Brisk</li>
    <li><svg width="8" height="8"><path d="M1 1l6 3-6 3z" fill="#7ea82b"/></svg>Ravin Tolland</li>
    <li><svg width="8" height="8"><path d="M1 1l6 3-6 3z" fill="#7ea82b"/></svg>Mira Castell</li>
    <li><svg width="8" height="8"><path d="M1 1l6 3-6 3z" fill="#7ea82b"/></svg>Mira Castell</li>
  </ul>
  <div class="more">View Complete Members List</div>
</section>

<section class="abs panel stat" style="left:203px">
  <div class="head">Most Active Users (5)</div>
  <ul>
    <li><svg width="8" height="8"><path d="M1 1l6 3-6 3z" fill="#7ea82b"/></svg>Mira Castell</li>
    <li><svg width="8" height="8"><path d="M1 1l6 3-6 3z" fill="#7ea82b"/></svg>Mira Castell</li>
    <li><svg width="8" height="8"><path d="M1 1l6 3-6 3z" fill="#7ea82b"/></svg>Mira Castell</li>
    <li><svg width="8" height="8"><path d="M1 1l6 3-6 3z" fill="#7ea82b"/></svg>Mira Castell</li>
    <li><svg width="8" height="8"><path d="M1 1l6 3-6 3z" fill="#7ea82b"/></svg>Mira Castell</li>
  </ul>
  <div class="more">View Complete Members List</div>
</section>

<section class="abs panel stat" style="left:386px">
  <div class="head light">Most Viewed Articles (5)</div>
  <ul>
    <li><svg width="8" height="8"><path d="M1 1l6 3-6 3z" fill="#7ea82b"/></svg>Test</li>
    <li><svg width="8" height="8"><path d="M1 1l6 3-6 3z" fill="#7ea82b"/></svg>Testing</li>
    <li><svg width="8" height="8"><path d="M1 1l6 3-6 3z" fill="#7ea82b"/></svg>Test</li>
    <li><svg width="8" height="8"><path d="M1 1l6 3-6 3z" fill="#7ea82b"/></svg>Test</li>
    <li><svg width="8" height="8"><path d="M1 1l6 3-6 3z" fill="#7ea82b"/></svg>Test</li>
  </ul>
  <div class="more right">Read More</div>
</section>

<section class="abs panel stat" style="left:570px">
  <div class="head">Most Article with Comments (1)</div>
  <ul>
    <li style="flex-direction:column;align-items:flex-start;gap:2px">Testing Mira<small>Comments (1)</small></li>
  </ul>
  <div class="more right">Read More</div>
</section>

<nav class="abs foot-nav">
  <span>Home</span><span>Hotels</span><span>Weather</span><span>Maps</span><span>Currency Converter</span><span>Contact</span><span>Privacy Policy</span><span>About Our Ads</span><span>Terms of Service</span>
</nav>

<footer class="abs footer">
  <div class="fcol" style="left:30px">
    <h4>POPULAR COUNTRIES</h4>
    <p>Australia , Austria , England ,<br>France , Germany , Japan<br>, Malaysia , Maldives , Switzerland<br>, Tanzania , Turkey , United Arab<br>Emirates ,</p>
  </div>
  <div class="fcol" style="left:290px">
    <h4>POPULAR CITIES</h4>
    <p>Athens , Athens , Athens , Athens ,<br>Athens , Athens , Athens , Athens ,<br>Athens , Athens , Athens , Athens ,<br>Athens , Athens , Athens , Athens ,<br>Athens , Athens , Athens , Athens ,</p>
  </div>
  <div class="fcol" style="left:530px">
    <h4>TOP WORLD HOTELS</h4>
    <p>Athens , Athens , Athens , Athens ,<br>Athens , Athens , Athens , Athens ,<br>Athens , Athens , Athens , Athens ,<br>Athens , Athens , Athens , Athens ,<br>Athens , Athens , Athens , Athens ,</p>
  </div>
  <div class="copy">© 2012 Kefor Inc. All rights reserved.</div>
</footer>

</body>
</html>
```